Sumvera financial services stationery design

We need business stationery designed with letterheads, business cards, with compliments and envelope for a business that offers tax and accounting services
Updates

Designs look the same

Target Market(s)

Small to medium businesses, individuals, Self managed superfunds

Industry/Entity Type

Business

Font styles to use
Serif
Other font styles liked:
• Atlanta

Colors
32a6d6
3277b5

Requirements
Must have
• Logo incorporated with all my stationery
• professional
Should not have
• Lots of colours
• Busy

```html
<!DOCTYPE html>
<html lang="en">
<head>
<meta charset="utf-8">
<title>Sumvera Financial Services – Business Card</title>
<link href="https://fonts.googleapis.com/css2?family=Cinzel:wght@400;600&family=Questrial&display=swap" rel="stylesheet">
<style>
  :root {
    --brand-blue: #1a78c2;
    --brand-sky: #32a6d6;
    --ink-dark: #3a3a3a;
    --ink-grey: #555555;
    --paper: #ffffff;
    --backdrop: #e9ecef;
  }
  * { margin: 0; padding: 0; box-sizing: border-box; }
  html, body { width: 1200px; height: 912px; overflow: hidden; }
  body {
    background: var(--backdrop);
    position: relative;
    font-family: "Questrial", sans-serif;
  }
  .card {
    position: absolute;
    width: 560px;
    height: 320px;
    border-radius: 16px;
    overflow: hidden;
    box-shadow: 0 6px 18px rgba(0,0,0,0.18);
  }

  /* Front */
  .card-front { left: 50px; top: 70px; background: var(--brand-blue); }
  .front-brand {
    position: absolute; left: 92px; top: 112px;
    display: flex; align-items: center; gap: 22px;
  }
  .brand-square {
    width: 74px; height: 74px; border-radius: 8px;
    background: var(--paper);
  }
  .brand-name {
    font-family: "Cinzel", serif; font-weight: 400;
    font-size: 58px; line-height: 1; color: var(--paper);
    letter-spacing: 1px;
  }
  .brand-tag {
    font-family: "Cinzel", serif; font-weight: 400;
    font-size: 15px; letter-spacing: 5px; color: var(--paper);
    margin-top: 6px;
  }
  .front-web {
    position: absolute; right: 40px; bottom: 34px;
    font-size: 16px; color: var(--paper);
  }

  /* Back */
  .card-back { right: 50px; bottom: 70px; background: var(--paper); }
  .back-band {
    position: absolute; left: 232px; right: 0; top: 128px; bottom: 0;
    background: var(--brand-blue);
  }
  .back-feature {
    position: absolute; left: 76px; top: 176px;
    width: 168px; height: 168px; border-radius: 18px;
    background: var(--brand-sky);
    border: 8px solid var(--paper);
  }
  .back-brand {
    position: absolute; right: 30px; top: 30px; text-align: left;
  }
  .back-brand .brand-name { font-size: 36px; color: var(--ink-dark); }
  .back-brand .brand-tag { font-size: 10px; letter-spacing: 3px; color: var(--ink-dark); margin-top: 3px; }
  .person { position: absolute; left: 36px; top: 100px; }
  .person-name {
    font-weight: 400; font-size: 22px; line-height: 1.1; letter-spacing: 0.5px;
    color: var(--brand-blue); -webkit-text-stroke: 0.6px var(--brand-blue);
  }
  .person-role { font-size: 15px; line-height: 1.2; color: var(--ink-grey); margin-top: 4px; }
  .contact {
    position: absolute; right: 28px; top: 144px;
    text-align: right; color: var(--paper); font-size: 14px; line-height: 1.45;
    list-style: none;
  }
  .contact li { display: flex; justify-content: flex-end; align-items: center; gap: 8px; }
  .contact .icon { width: 10px; height: 10px; flex: none; }
  .contact .spacer { width: 10px; flex: none; }
</style>
</head>
<body>

<section class="card card-front" aria-label="Business card front">
  <div class="front-brand">
    <span class="brand-square"></span>
    <div>
      <div class="brand-name">SUMVERA</div>
      <div class="brand-tag">FINANCIAL SERVICES</div>
    </div>
  </div>
  <div class="front-web">www.sumverafinance.com</div>
</section>

<section class="card card-back" aria-label="Business card back">
  <div class="back-band"></div>
  <div class="back-feature"></div>

  <div class="back-brand">
    <div class="brand-name">SUMVERA</div>
    <div class="brand-tag">FINANCIAL SERVICES</div>
  </div>

  <div class="person">
    <div class="person-name">DANIEL REYES</div>
    <div class="person-role">Founder</div>
  </div>

  <ul class="contact">
    <li>482 Harbor View Rd.<span class="spacer"></span></li>
    <li>Coral Point, FL 33400<span class="spacer"></span></li>
    <li>555-014-2287
      <svg class="icon" viewBox="0 0 10 10"><path d="M2 1l2 2-1 1.2c.6 1.2 1.5 2.1 2.8 2.8L7 6l2 2-1.2 1.2C4.5 9 1 5.5.8 2.2z" fill="#fff"/></svg>
    </li>
    <li>info@sumverafinance.com
      <svg class="icon" viewBox="0 0 10 10"><rect x="0.5" y="2" width="9" height="6" fill="none" stroke="#fff"/><path d="M0.5 2l4.5 3.5L9.5 2" fill="none" stroke="#fff"/></svg>
    </li>
    <li>www.sumverafinance.com
      <svg class="icon" viewBox="0 0 10 10"><circle cx="5" cy="5" r="4.3" fill="none" stroke="#fff"/><ellipse cx="5" cy="5" rx="1.8" ry="4.3" fill="none" stroke="#fff"/><path d="M0.7 5h8.6" stroke="#fff"/></svg>
    </li>
  </ul>
</section>

</body>
</html>
```